Northfield Prairie Outfitters Gift Card

We need a a design for a plastic gift card. We have a firearms shop and would like it to reflex it. One side... our website is northfieldprairieout.example.. Here are the requirements from the printer;

Gift Card Printing Guidelines

Preferred Applications: Quark Express, Illustrator, PhotoShop. In some cases we will accept other formats.
Additional details:
Quark: Make sure to include: all screen and printer fonts and support images: photos, logos, etc. Do NOT use Style Command to create bold, italic, shadowed, or outlined text. Instead use exact fonts. Use "Collect for Output" to create the folder and files to send.

Illustrator: Make sure all fonts are outlined and send .ai file along with a saved .pdf file.

Photoshop: Include all layers & fonts used. In addition create a duplicate flattened file in .tif format.

Bleed (if you have an image, graphic or color up to the edge of the card you must add a bleed): All card printing jobs require a minimum of 1/8" (3mm.) outside the final trim area for bleed . Avoid placing text and other important elements within 1/8" (3mm.) of the edge of your card to allow for slight movement during cutting. See illustration for details:

(Please note that the Card Die Line is 3 3/8 x 2 1/8).

Resolution: No less than 300dpi. If the card back contains text (black and white) and is created in Photoshop please create in 1200dpi. Text for card backs will reproduce the best if created in Illustrator and must be solid black line art.

Color: Artwork based on photographs should be built using CMYK (4-color process). If pantone colors are used in your artwork please convert them to CMYK. Vector graphic artwork in one to three colors can be made from pantone colors.

If possible include a PDF file as a quality control guide for us to assure that printing file is opening up properly as you intended. If you do not have Adobe Acrobat please send a .jpg or .tif file. PDF files are not recommended for actual printing due to color shifting problems unless created in Illustrator and not optimized for web viewing.

When printing on plastic exact colors cannot be guarantied, there can be a 15% shift in colors. If the job needs to match other printed material's colors or previous printed colors please send an actual sample of the required colors.

I have attached two files.. one is the layout and the second are some samples printed before by the company..

```html
<!DOCTYPE html>
<html lang="en">
<head>
<meta charset="utf-8">
<title>Northfield Prairie Outfitters Gift Card</title>
<link rel="stylesheet" href="https://fonts.googleapis.com/css2?family=Crimson+Text:wght@400&family=Roboto+Condensed:wght@700&display=swap">
<style>
  :root {
    --page-bg: #e4e4e4;
    --sky-top: #aab2ba;
    --sky-mid: #c4c2bd;
    --horizon: #d3a27a;
    --dusk: #3a2e26;
    --reeds: #0b0b0b;
    --text-light: #ffffff;
    --brand-gold: #eab91f;
    --brand-green: #3d6a2b;
    --badge-ring: #2f2f2f;
    --badge-face: #f2f2f2;
  }
  * { margin: 0; padding: 0; box-sizing: border-box; }
  html, body {
    width: 1200px;
    height: 900px;
    overflow: hidden;
    background: var(--page-bg);
  }
  .gift-card {
    position: absolute;
    left: 78px;
    top: 88px;
    width: 1045px;
    height: 640px;
    border-radius: 30px;
    overflow: hidden;
    background: var(--reeds);
  }
  .hunting-scene {
    position: absolute;
    inset: 0;
    background:
      radial-gradient(ellipse 260px 300px at 760px 330px, rgba(11,11,11,0.95) 0%, rgba(11,11,11,0.75) 45%, rgba(11,11,11,0) 100%),
      radial-gradient(ellipse 200px 360px at 980px 300px, rgba(11,11,11,0.85) 0%, rgba(11,11,11,0) 100%),
      radial-gradient(ellipse 520px 180px at 300px 330px, rgba(40,32,26,0.7) 0%, rgba(40,32,26,0) 100%),
      linear-gradient(180deg,
        var(--sky-top) 0%,
        var(--sky-mid) 28%,
        var(--horizon) 50%,
        var(--dusk) 62%,
        var(--reeds) 72%,
        var(--reeds) 100%);
  }
  .card-title {
    position: absolute;
    left: 72px;
    top: 10px;
    font-family: "Crimson Text", serif;
    font-weight: 400;
    font-size: 110px;
    line-height: 1;
    color: var(--text-light);
    text-shadow: 2px 3px 4px rgba(0, 0, 0, 0.45);
  }
  .partner-badge {
    position: absolute;
    left: 872px;
    top: 18px;
  }
  .brand {
    position: absolute;
    left: 80px;
    top: 490px;
    display: flex;
    align-items: center;
    gap: 16px;
  }
  .brand-mark {
    width: 44px;
    height: 44px;
    border-radius: 50%;
    background: var(--brand-green);
  }
  .brand-name {
    font-family: "Roboto Condensed", sans-serif;
    font-weight: 700;
    font-size: 30px;
    color: var(--brand-gold);
  }
  .contact {
    position: absolute;
    left: 638px;
    top: 469px;
    font-family: "Roboto Condensed", sans-serif;
    font-weight: 700;
    font-size: 16px;
    line-height: 20.5px;
    color: var(--text-light);
    list-style: none;
  }
</style>
</head>
<body>
  <section class="gift-card">
    <div class="hunting-scene" role="img" aria-label="Photograph of a hunter in a cap aiming a shotgun, silhouetted among tall reeds against a sunset sky"></div>
    <h1 class="card-title">Gift Card</h1>
    <svg class="partner-badge" width="112" height="112" viewBox="0 0 112 112" aria-hidden="true">
      <circle cx="56" cy="56" r="54" fill="var(--badge-ring)"/>
      <circle cx="56" cy="56" r="44" fill="var(--badge-face)"/>
    </svg>
    <div class="brand">
      <span class="brand-mark"></span>
      <span class="brand-name">Northfield Prairie Outfitters</span>
    </div>
    <ul class="contact">
      <li>Email: Sales@northfieldprairieout.example</li>
      <li>Phone No: 855- Gear 4 Less Or 855-555-0142</li>
      <li>Address: 412 Prairie Ridge Road</li>
      <li>Northfield, Ms. 39000</li>
    </ul>
  </section>
</body>
</html>
```